Book Cover Design for Educational Assessment Book

We are a publisher based in Singapore. We need a book cover design for an educational assessment book titled "Keystone Tier Advanced Numeracy Drill Compendium". The book is targeted at high school students, hence the design should look professional and not overly fanciful. This book is the first in a series. Subsequent books will have the same design but of different theme colours. Designers need to take note that the design must allow for different theme colours to be used. Please refer to the attached file 'Syllabus' for the mathematical concepts taught in our book.

Target Market(s)

Singapore Keystone Tier Students/ High School Students

Industry/Entity Type

Education

Requirements
Must have
• 1. A Space for Company Logo on top right
• 2. A Space for ISBN number on bottom right (to be provided later)
• 3. Book Highlights:
• a. "The Most Comprehensive Advanced Numeracy Drill Compendium"
• b. "More than 1000 Questions"
• c. "With Step-by-Step Complete Solutions"
• d. "Latest NCA Syllabus - Syllabus 7132"
• e. "Questions Booklet"
Nice to have
• Nice to have a theme colour, so we can allocate different colours to subsquent books in the same series.
• Nice to have appropriate and simple mathematical graphics or formulae.
Should not have
• Cartoons, Photographs, Flamboyant Graphics

```html
<!DOCTYPE html>
<html lang="en">
<head>
<meta charset="utf-8">
<title>Advanced Numeracy Drill Compendium — Questions Booklet</title>
<link rel="stylesheet" href="https://fonts.googleapis.com/css2?family=Open+Sans:wght@400;700&display=swap">
<style>
  :root {
    --cover-bg: #a4d7d8;
    --spine-band: #22a6a7;
    --highlight-band: #62baba;
    --title-teal: #0f6b69;
    --text-grey: #555b5c;
    --brand-teal: #14807d;
    --isbn-panel: #c4e6e6;
  }
  * { margin: 0; padding: 0; box-sizing: border-box; }
  html, body { width: 900px; height: 1200px; overflow: hidden; }
  body { background: var(--cover-bg); font-family: "Open Sans", Arial, sans-serif; }
  .cover { position: relative; width: 900px; height: 1200px; background: var(--cover-bg); overflow: hidden; }
  .side-band { position: absolute; left: 828px; top: 0; width: 72px; height: 1200px; background: var(--spine-band); }

  .publisher { position: absolute; left: 660px; top: 16px; width: 140px; text-align: center; }
  .publisher-mark { display: block; width: 96px; height: 96px; margin: 0 auto 18px; border: 3px solid var(--brand-teal); border-radius: 50%; }
  .publisher-name { font-size: 14px; font-weight: 700; color: var(--brand-teal); white-space: nowrap; }

  .kicker, .title-line, .subtitle { position: absolute; left: 54px; line-height: 1; white-space: nowrap; font-weight: 400; }
  .kicker { top: 202px; font-size: 38px; letter-spacing: 5px; color: var(--text-grey); }
  .title-line { font-size: 118px; color: var(--title-teal); letter-spacing: -1px; left: 52px; }
  .title-line.first { top: 243px; }
  .title-line.second { top: 355px; }
  .subtitle { top: 481px; font-size: 58px; color: var(--text-grey); letter-spacing: 3px; }
  h1 { font-weight: 400; }

  .highlight { position: absolute; left: 0; width: 566px; background: var(--highlight-band); color: var(--text-grey); }
  .hl-syllabus { top: 579px; height: 79px; display: flex; align-items: center; padding-left: 90px; }
  .hl-syllabus .big { font-size: 76px; line-height: 1; letter-spacing: -2px; }
  .hl-syllabus .stack { font-size: 29px; line-height: 0.92; margin-left: 8px; }

  .hl-solutions { top: 691px; height: 95px; display: flex; align-items: center; padding-left: 92px; }
  .hl-solutions .stack { font-size: 26px; line-height: 0.9; text-align: center; }
  .hl-solutions .big { font-size: 46px; line-height: 1; margin-left: 6px; letter-spacing: 1px; }

  .hl-questions { top: 818px; height: 112px; padding-left: 92px; padding-top: 4px; }
  .hl-questions .row { display: flex; align-items: center; height: 66px; }
  .hl-questions .stack { font-size: 27px; line-height: 0.95; }
  .hl-questions .big { font-size: 74px; line-height: 1; margin-left: 2px; letter-spacing: -2px; }
  .hl-questions .label { font-size: 34px; letter-spacing: 5px; line-height: 1; margin-left: 4px; }

  .hl-booklet { top: 960px; height: 106px; padding-left: 94px; padding-top: 4px; }
  .hl-booklet .line { font-size: 46px; line-height: 1.05; letter-spacing: 1px; }

  .isbn-space { position: absolute; left: 578px; top: 1104px; width: 208px; height: 60px; background: var(--isbn-panel); }
</style>
</head>
<body>
<main class="cover">
  <div class="side-band"></div>

  <div class="publisher">
    <span class="publisher-mark"></span>
    <span class="publisher-name">Meridian Learning</span>
  </div>

  <p class="kicker">THE MOST COMPREHENSIVE</p>
  <h1>
    <span class="title-line first">ADVANCED</span>
    <span class="title-line second">NUMERACY</span>
  </h1>
  <p class="subtitle">DRILL COMPENDIUM</p>

  <section class="highlight hl-syllabus">
    <span class="big">LATEST</span>
    <span class="stack">NCA 7132<br>SYLLABUS</span>
  </section>

  <section class="highlight hl-solutions">
    <span class="stack">STEP<br>BY<br>STEP</span>
    <span class="big">COMPLETE<br>SOLUTIONS</span>
  </section>

  <section class="highlight hl-questions">
    <div class="row">
      <span class="stack">MORE<br>THAN</span>
      <span class="big">1000</span>
    </div>
    <div class="label">QUESTIONS</div>
  </section>

  <section class="highlight hl-booklet">
    <div class="line">QUESTIONS</div>
    <div class="line">BOOKLET</div>
  </section>

  <div class="isbn-space" role="img" aria-label="Reserved space for ISBN barcode"></div>
</main>
</body>
</html>
```